NZ First of it's kind solutions directory and marketplace for busy Mums needs a business card design

We need a business card design for our new nationwide business in NZ (long term plans to go global). We provide solutions to the everyday challenges that busy Mums face by connecting them with quality communities and suppliers of carefully selected, relevant products and services. We sell direct via our online marketplace. The final design should communicate our values of inclusivity, quality and smart solutions. Colours should incorporate our logo colour palette of #477077 and #6ba8b2. Our website is at https://www.brightnestly.com

Target Market(s)

busy Mums, Age 28 – 50, female, income over $100K, location main centres NZ primarily but NZ wide. Is likely juggling work or career with a young family. Probably had hobbies which have fallen by the wayside.
-Wants to succeed in her chosen career without compromising on family life
-to successfully juggle her career without feeling like she is compromising her children
- Is time poor, something always has to give and it’s generally her health (she’ll stay up late, get stressed)
- probably ex corporate or professional career. Has discretional income

Industry/Entity Type

Business

Contact Information for Business Card

Jodie Farnsworth, Founder, BrightNestly.com (Strapline Browse; Pick; Sorted), 48 Kowhai Terrace, Hillsborough, Auckland 1058, New Zealand. Mob: 021 437 518 Ph: +64 (0)9 584 7163

Font styles to use
Other font styles liked:
• Raleway, and/or Architects Daughter

Colors
00a990
33b8a4
86cfc6
cfeae6

Requirements
Must have
• the above details, streamline. the logo and colours associated with those logos
Should not have
• foil or metallic colours

```html
<!DOCTYPE html>
<html lang="en">
<head>
<meta charset="utf-8">
<title>BrightNestly Business Card</title>
<link rel="stylesheet" href="https://fonts.googleapis.com/css2?family=Arimo:wght@400;700&display=swap">
<style>
  :root {
    --stage: #1e1e1e;
    --paper: #ffffff;
    --teal-dark: #477077;
    --teal-light: #6ba8b2;
    --ink: #222222;
    --ink-soft: #4a4a4a;
    --back-edge: #55858c;
  }
  * { margin: 0; padding: 0; box-sizing: border-box; }
  html, body {
    width: 1200px;
    height: 900px;
    overflow: hidden;
    background: var(--stage);
    font-family: "Arimo", Arial, sans-serif;
  }
  .canvas { position: relative; width: 1200px; height: 900px; }

  .card {
    position: absolute;
    top: 170px;
    width: 347px;
    height: 561px;
    box-shadow: 2px 3px 6px rgba(0,0,0,0.6);
  }
  .card--front { left: 259px; background: var(--paper); }
  .card--back {
    left: 631px;
    background: radial-gradient(circle at 62% 28%, #6eaab3 0%, var(--teal-light) 30%, #5f959d 70%, var(--back-edge) 100%);
  }

  /* Front: brand line */
  .brand {
    position: absolute;
    top: 176px;
    left: 0;
    width: 100%;
    display: flex;
    align-items: center;
    justify-content: center;
    gap: 12px;
  }
  .brand__dot {
    width: 30px;
    height: 30px;
    border-radius: 50%;
    background: var(--teal-dark);
  }
  .brand__name {
    font-size: 33px;
    font-weight: 700;
    color: var(--teal-dark);
    letter-spacing: -0.5px;
  }

  /* Front: contact block */
  .contact {
    position: absolute;
    top: 343px;
    left: 0;
    width: 100%;
    text-align: center;
    color: var(--ink);
  }
  .contact__name {
    font-size: 20px;
    font-weight: 700;
    line-height: 24px;
    color: var(--ink-soft);
    letter-spacing: 0.3px;
  }
  .contact__name .first { color: var(--teal-dark); }
  .contact__role {
    font-size: 15px;
    line-height: 18px;
    color: var(--ink);
  }
  .rule {
    width: 140px;
    height: 1px;
    margin: 0 auto;
    background: var(--teal-light);
  }
  .rule--top { margin-top: 10px; margin-bottom: 6px; }
  .rule--bottom { margin-top: 8px; margin-bottom: 14px; }
  .contact__line {
    font-size: 16px;
    line-height: 20.5px;
  }
  .contact__label { font-weight: 700; color: var(--teal-dark); }
  .address {
    font-size: 16px;
    line-height: 20px;
  }

  /* Back */
  .back__mark {
    position: absolute;
    left: 84px;
    top: 170px;
    width: 180px;
    height: 180px;
    border-radius: 50%;
    background: var(--paper);
  }
  .back__url {
    position: absolute;
    top: 496px;
    left: 0;
    width: 100%;
    text-align: center;
    font-size: 21px;
    color: var(--paper);
  }
</style>
</head>
<body>
<main class="canvas">
  <section class="card card--front">
    <div class="brand">
      <span class="brand__dot"></span>
      <span class="brand__name">BrightNestly</span>
    </div>
    <div class="contact">
      <p class="contact__name"><span class="first">JODIE</span> FARNSWORTH</p>
      <p class="contact__role">Founder</p>
      <div class="rule rule--top"></div>
      <p class="contact__line"><span class="contact__label">P:</span> 021 437 518</p>
      <p class="contact__line"><span class="contact__label">M:</span> +64 (0)9 584 7163</p>
      <p class="contact__line"><span class="contact__label">W:</span> www.BrightNestly.com</p>
      <div class="rule rule--bottom"></div>
      <p class="address">48 Kowhai Terrace, Hillsborough</p>
      <p class="address">Auckland 1058, New Zealand</p>
    </div>
  </section>

  <section class="card card--back">
    <span class="back__mark"></span>
    <p class="back__url">www.BrightNestly.com</p>
  </section>
</main>
</body>
</html>
```